New Wordpress theme/Update website

Many of our plug ins are in need to updating and Id like to make my website more modern. We are a Chiropractic office and our logo colors are black, white and red. My goal is to have an updated look that allows me to make simple edits(such as i currently have limitations on # of employee profiles) and stay operating well on my corvexhost hosting compnay ive prepaid for a few years for. And to keep working well on the mobile platform. Can email all the edits id like to make to www.DrMarcusHalvern.com Thanks
Here are the exact edits:
bright red, colors, etc
Change NEw patient Tab from coupon to special offers-Change word download on NP forms
Remove blog text on sites
UPDATE VIDSTREAMO videos-Upload all from PK-So the VidStreamo link on site is relevant-REmove 2 tabs on top
Update FAQ tab to our recent edited sheet on common myths
Update office hours
Testimonial videos on conditions page -LBP-back pain video, etc. and one landing page or smaller icon on home page but when you click it pops up larger over website.
Keep video on front but put elsewhere. Lower on office tour with pics, but video icon is first.
add MOST INSURANCES ACCEPTED
Add Heal Strong Walk Strong Live Strong
Capitalize We diagnose & address the root cause to your health problem
Eliminate Home Exercise Tab?
Instead of video , picture office tour that rotates-use blur iphone pics
black bright red and white-black and white backgrounds alternate as you scroll down page
New testimonial videos -with Me and DrW-LINKS FOR PATIENT VIDEOS or MY VIDEOS-Educational
Unlimited Staff profiles-easy to change
Scrolling down home page-Pain pic on top, then office team pic then below that office tour, then map
Call to action tabs-Free Consult-Free Mechanical Massage, MASSAGE coupon
Change about us to meet the team?
Single space my bullets -Profile
Merge Location into Contact Us
all conditions on home page on one tab
Pain relief picture? Heal Strong Walk Strong Live Strong tagline-On top wording explains what we do-Root cause. Then 3 clickable buttons below-New patients-Scheduling-Meet the team-Back Brace-Vitamins?
update layout, pictures(thoroughout), coloring, and flow of the main page
about us page also layout wayyyyyyyyyy to wordy
services pages again layout and wordy, bulleted points not necessary when listing services
personally interesting facts adn stas are not needed and articles ( if that stuff was important to you ass links for them)
FAQ is its own tab why is it also under services ? one place only (layout on this page)
weightloss tab isnt even avalible...page not found
is Norvale Imaging and Spinal Review a necessary tab ?
for the supplements it has no details, simply directs you to nutrovance page ( not in a new tab either )which I feel can be confusing. We use their products but its listed under services. what are those services in regards to supplements, know what I mean?
for location the plotmap map is unable to load map correctly......not helpful. also why is the description of what we do within the directions on how to find us? and when clicking the lionk for directions this message pops up 'There was an error geocoding your location. Check the address and try again"
video testimonals need major updating
also on blog/news you have misconceptions abouit chiro, redundant, these type of things should be on the FAQ page.
social media tabs, relevance of the first and last button
Also their supplement tab leads to our own page...explains to picks then a link for separate landing page to buy , include velumora that way. And stress support in office.
Go into their practice area tab and a short way down they have what they offer there but it’s in a box that you go left or right to see what they offer. It’s neater and still gets point across
They do this again under conditions. I’d like to see this utilized for our sight :)
Also like you mentioned we had but I couldn’t see. Is at the bottom of each page was a click to schedule appointment that’s 👌🏼 Perfect
https://www.qrtvhealthhub.com/
http://www.zkwnstudio.com/
http://www.brightfieldvitalsupply.com/
Refer to https://tallowmerespine.com/ to see how conditions treated was put in
OR EVOLVING PIC
CODING is already included on thebudget for this website.

```html
<!DOCTYPE html>
<html lang="en">
<head>
<meta charset="UTF-8">
<title>Eastbrook Chiropractic – Why Choose Us</title>
<link rel="stylesheet" href="https://fonts.googleapis.com/css2?family=Alegreya:wght@400&family=Source+Sans+3:wght@400;600&display=swap">
<style>
  :root {
    --paper: #ffffff;
    --ink: #111111;
    --brand-red: #e0202c;
    --text-on-paper: #333333;
    --text-on-ink: #e8e8e8;
    --button-text: #ffffff;
  }
  * { box-sizing: border-box; margin: 0; padding: 0; }
  html, body {
    width: 1200px;
    height: 575px;
    overflow: hidden;
    background: var(--paper);
  }
  .band {
    width: 1200px;
    display: flex;
    flex-direction: column;
    align-items: center;
    justify-content: center;
    text-align: center;
  }
  .band--light { background: var(--paper); color: var(--text-on-paper); }
  .band--dark { background: var(--ink); color: var(--text-on-ink); }
  .band--intro { height: 180px; }
  .band--refer { height: 170px; }
  .band--ages { height: 225px; }
  .band__heading {
    font-family: "Alegreya", Georgia, serif;
    font-weight: 400;
    font-size: 35px;
    line-height: 44px;
    color: var(--brand-red);
  }
  .band__text {
    width: 880px;
    margin-top: 14px;
    font-family: "Source Sans 3", "Source Sans Pro", Arial, sans-serif;
    font-size: 14.5px;
    line-height: 20px;
  }
  .schedule-button {
    display: inline-flex;
    align-items: center;
    justify-content: center;
    gap: 10px;
    width: 150px;
    height: 40px;
    margin-top: 22px;
    background: var(--brand-red);
    color: var(--button-text);
    font-family: "Source Sans 3", "Source Sans Pro", Arial, sans-serif;
    font-size: 14px;
    font-weight: 600;
    text-decoration: none;
  }
  .schedule-button svg { width: 14px; height: 15px; }
</style>
</head>
<body>
  <section class="band band--light band--intro">
    <h1 class="band__heading">We Understand Your Apprehension</h1>
    <p class="band__text">Chiropractic care is now part of mainstream health care. We offer the best facility, the best hours, the best care and the most options under one roof, with a master of each trade on our team. See Meet the Team for every staff member and the services they provide.</p>
  </section>

  <section class="band band--dark band--refer">
    <h2 class="band__heading">Willingness To Refer</h2>
    <p class="band__text">At Eastbrook, we work closely with the medical community. Our staff is trained to recognize which conditions respond to chiropractic care and which require a medical referral.</p>
  </section>

  <section class="band band--light band--ages">
    <h2 class="band__heading">Customized Care for All Ages</h2>
    <p class="band__text">WE DIAGNOSE &amp; ADDRESS THE ROOT CAUSE OF YOUR HEALTH PROBLEM with safe, research-based care, a natural alternative to drugs or surgery. We see infants, pregnant mothers, children of all ages and sports injuries, each on a plan built for them.</p>
    <a class="schedule-button" href="#schedule">Schedule Today!
      <svg viewBox="0 0 14 15" aria-hidden="true">
        <rect x="0" y="2" width="14" height="13" rx="1.5" fill="#fff"/>
        <rect x="3" y="0" width="2" height="4" rx="1" fill="#fff"/>
        <rect x="9" y="0" width="2" height="4" rx="1" fill="#fff"/>
        <rect x="0" y="5" width="14" height="1" fill="#e0202c"/>
        <g fill="#e0202c">
          <rect x="2" y="7.5" width="2" height="2"/><rect x="6" y="7.5" width="2" height="2"/><rect x="10" y="7.5" width="2" height="2"/>
          <rect x="2" y="11" width="2" height="2"/><rect x="6" y="11" width="2" height="2"/><rect x="10" y="11" width="2" height="2"/>
        </g>
      </svg>
    </a>
  </section>
</body>
</html>
```